UI/UX Design for AI Photo-to-Video Web Platform (Figma)

I am looking for a modern, high-converting redesign for my Next.js-based web platform. The service allows users to transform old photos into vibrant memories using AI. The design needs to be clean, intuitive, and "mobile-ready" (responsive).
Key Features to Visualize on the Homepage:
Photo Restoration & Colorization: A clear "before/after" visual showing a black-and-white photo turning into a high-quality color photo.
Photo-to-Video Animation: A visual representation of how both B&W and color photos are transformed into dynamic video clips.
Story Creation: A section showing how these photos and videos are combined into a single "Story Video" with background music.
Scope of Work:
Homepage Redesign: A hero section with the core value proposition and a visual walkthrough of the process.
Service/Internal Pages: Redesigning the functional pages where users upload files and manage their projects.
Responsive Design: While the focus is desktop, the layout must be designed with a "Mobile-First" mindset for easy porting to a mobile app later.
Technical Requirements for the Designer:
Tool: Must be designed in Figma.
Structure: Use Figma Auto Layout and Components for all elements (buttons, inputs, cards).
Design System: Provide a clear style guide (Typography, Color Palette, Spacing).
Assets: All icons should be in SVG format.
Style Preference:
Modern, sleek, and trustworthy.
Since the product is about "memories," the vibe should be emotional yet technologically advanced (AI-driven).

```html
<!DOCTYPE html>
<html lang="en">
<head>
<meta charset="utf-8">
<title>Hueframe.ai – Images</title>
<link href="https://fonts.googleapis.com/css2?family=Inter:wght@400;500;600;700&display=swap" rel="stylesheet">
<style>
:root{
  --bg:#ffffff;
  --ink:#16181d;
  --muted:#5b6068;
  --soft:#8a8f97;
  --blue:#1a73f0;
  --blue-soft:#dfeafc;
  --panel:#ececee;
  --card:#ffffff;
  --label:#dcdde0;
  --line:#d4d6da;
  --red:#ef4444;
  --orange:#f5a524;
  --orange-text:#ea7a0a;
  --green:#1f9d55;
  --green-soft:#e3f5ea;
}
*{box-sizing:border-box;margin:0;padding:0}
html,body{width:1200px;height:912px;overflow:hidden}
body{font-family:"Inter",sans-serif;color:var(--ink);background:var(--bg);position:relative;white-space:nowrap}
svg{flex-shrink:0}
.glow{position:absolute;left:600px;top:-120px;width:650px;height:300px;border-radius:50%;background:radial-gradient(closest-side,rgba(180,208,250,.55),rgba(255,255,255,0));pointer-events:none}
.abs{position:absolute}
.brand{left:62px;top:16px;font-size:17px;font-weight:700;letter-spacing:-.2px}
.tabs{left:62px;top:50px;width:304px;height:34px;border:1px solid var(--line);border-radius:17px;background:#f6f7f9}
.tab{position:absolute;top:1px;display:flex;align-items:center;gap:8px;height:30px;border-radius:15px;font-size:10px;font-weight:600;white-space:nowrap}
.tab--active{left:1px;width:81px;padding-left:11px;background:var(--blue);color:#fff}
.tab--video{left:102px}
.tab--studio{left:229px}
.tab svg{width:14px;height:14px}
.pill{height:26px;border-radius:13px;display:flex;align-items:center;gap:4px;padding:0 8px;font-size:9.5px;white-space:nowrap}
.pill--storage{left:830px;top:12px;border:1px solid var(--line);background:#fff}
.pill--credits{left:941px;top:12px;background:var(--blue-soft)}
.pill b{font-weight:700}
.pill span{color:var(--soft)}
.user{right:95px;top:19px;font-size:10px;font-weight:600}
.avatar{left:1111px;top:12px;width:26px;height:26px;border-radius:50%;background:linear-gradient(135deg,#e9c3a6,#b98a6c)}
.panel{background:var(--panel);border-radius:18px}
.upload{left:63px;top:109px;width:1074px;height:187px}
.section-head{position:absolute;left:17px;display:flex;align-items:center;gap:8px}
.section-head h2{font-size:13px;font-weight:600}
.section-head p{font-size:10px;color:var(--muted);margin-left:6px}
.btn-select{left:972px;top:9px;width:90px;height:25px;border-radius:7px;background:var(--blue);color:#fff;font-size:10px;font-weight:600;display:flex;align-items:center;justify-content:center;gap:5px}
.dropzone{left:6px;top:44px;width:1062px;height:137px;background:#fff;border-radius:14px}
.dropzone-inner{position:absolute;inset:6px;border:1px dashed #c5c8cd;border-radius:10px;display:flex;flex-direction:column;align-items:center;justify-content:center;gap:9px}
.dropzone-inner h3{font-size:13.5px;font-weight:500}
.dropzone-inner p{font-size:8.5px;color:var(--muted)}
.gallery{left:63px;top:309px;width:1074px;height:537px}
.disclaimer{right:18px;top:15px;display:flex;align-items:center;gap:6px;font-size:10px;font-weight:500;color:var(--orange-text)}
.tile{position:absolute;width:250px;height:212px;border-radius:14px;background:var(--label);overflow:hidden}
.tile-label{height:25px;display:flex;align-items:center;justify-content:center;gap:6px;font-size:8.5px;font-weight:500}
.tile-body{position:absolute;left:0;top:25px;width:250px;height:187px;border-radius:14px;background:var(--card);display:flex;align-items:center;justify-content:center;font-size:10px;color:var(--soft)}
.photo-bw{background:linear-gradient(160deg,#8c8c8c 0%,#4a4a4a 45%,#1f1f1f 100%)}
.photo-color{background:linear-gradient(160deg,#5f8f4e 0%,#2f4e2c 40%,#1c2540 75%,#242a44 100%)}
.dl{position:absolute;right:6px;bottom:6px;width:30px;height:30px;border-radius:9px;background:var(--blue);display:flex;align-items:center;justify-content:center}
.badge{display:inline-flex;align-items:center;gap:3px;height:12px;padding:0 5px;border-radius:6px;border:1px solid var(--green);background:var(--green-soft);color:var(--green);font-size:7px}
.action{position:absolute;left:793px;width:262px;height:25px;border-radius:8px;display:flex;align-items:center;justify-content:center;font-size:10px;font-weight:500}
.action svg{position:absolute;left:12px}
.action--outline{border:1px solid var(--line);background:#f7f7f8}
.action--danger{border:1px solid var(--red);color:var(--red);background:#f7f7f8}
.action--generate{background:var(--orange);color:#fff;font-weight:600}
.divider{position:absolute;left:0;top:269px;width:1074px;height:1px;background:#dadcdf}
.timing{position:absolute;left:793px;top:282px;width:262px;height:175px;border-radius:12px;background:#e2e3e5;display:flex;flex-direction:column;align-items:center;justify-content:center;gap:5px}
.timing p{font-size:10px;color:var(--muted)}
.timing strong{font-size:19px;font-weight:500}
</style>
</head>
<body>
<div class="glow"></div>

<header>
  <div class="abs brand">Hueframe.ai</div>
  <nav class="abs tabs">
    <div class="tab tab--active">
      <svg viewBox="0 0 16 16" fill="none" stroke="#fff" stroke-width="1.4"><rect x="2" y="2" width="12" height="12" rx="3"/><circle cx="6" cy="6" r="1.3"/><path d="M2.5 12l4-4 3 3 2-2 2 2"/></svg>Images
    </div>
    <div class="tab tab--video">
      <svg viewBox="0 0 16 16" fill="none" stroke="#16181d" stroke-width="1.3"><circle cx="8" cy="8" r="6.3"/><path d="M6.6 5.5v5l4-2.5z"/></svg>Video Animations
    </div>
    <div class="tab tab--studio">
      <svg viewBox="0 0 16 16" fill="none" stroke="#16181d" stroke-width="1.3"><path d="M8 1.8a4.6 4.6 0 0 0-2.6 8.4V12h5.2v-1.8A4.6 4.6 0 0 0 8 1.8z"/><path d="M6.2 14h3.6M8.6 5 7.2 7.6h1.7L7.6 10"/></svg>Studio
    </div>
  </nav>
  <div class="abs pill pill--storage">
    <svg width="14" height="12" viewBox="0 0 16 14" fill="none" stroke="#1a73f0" stroke-width="1.5"><path d="M4.5 11H4a3 3 0 0 1-.3-6A4.5 4.5 0 0 1 12.4 4 3.5 3.5 0 0 1 12 11h-.5"/><path d="M8 13V7M5.8 9 8 6.8 10.2 9"/></svg>
    <b>114 MB</b><span>/ 1.0 GB</span>
  </div>
  <div class="abs pill pill--credits">
    <svg width="12" height="12" viewBox="0 0 12 12"><circle cx="6" cy="6" r="6" fill="#1a73f0"/><path d="M6 2.5 7 5l2.5 1L7 7 6 9.5 5 7 2.5 6 5 5z" fill="#fff"/></svg>
    <b>4740</b><span>Credits</span>
  </div>
  <div class="abs user">Ada Varga</div>
  <div class="abs avatar" role="img" aria-label="User profile photo"></div>
</header>

<section class="abs panel upload">
  <div class="section-head" style="top:13px">
    <svg width="16" height="14" viewBox="0 0 16 14" fill="none" stroke="#1a73f0" stroke-width="1.5"><path d="M4.5 11H4a3 3 0 0 1-.3-6A4.5 4.5 0 0 1 12.4 4 3.5 3.5 0 0 1 12 11h-.5"/><path d="M8 13V7M5.8 9 8 6.8 10.2 9"/></svg>
    <h2>Upload Images</h2>
    <p>Upload photos to generate vintage and real color versions.</p>
  </div>
  <div class="abs btn-select">
    <svg width="11" height="12" viewBox="0 0 12 14" fill="none" stroke="#fff" stroke-width="1.3"><path d="M7.5 1H3a1.5 1.5 0 0 0-1.5 1.5v9A1.5 1.5 0 0 0 3 13h6a1.5 1.5 0 0 0 1.5-1.5V4z"/><path d="M7.5 1v3h3M4 7.5h4M4 10h3"/></svg>Select Files
  </div>
  <div class="abs dropzone">
    <div class="dropzone-inner">
      <h3>Drag and drop images here</h3>
      <p>Maximum 20 images • 100MB total • JPG, PNG, GIF, TIFF up to 10MB each</p>
    </div>
  </div>
</section>

<section class="abs panel gallery">
  <div class="section-head" style="top:14px">
    <svg width="14" height="14" viewBox="0 0 16 16" fill="none" stroke="#1a73f0" stroke-width="1.4"><rect x="2" y="2" width="12" height="12" rx="3"/><circle cx="6" cy="6" r="1.3"/><path d="M2.5 12l4-4 3 3 2-2 2 2"/></svg>
    <h2>Images</h2>
    <p>Each row shows Original, Vintage Color, and Real Color.</p>
  </div>
  <div class="abs disclaimer">
    <svg width="12" height="12" viewBox="0 0 12 12"><circle cx="6" cy="6" r="6" fill="#ea7a0a"/><path d="M6 5.2v3.6" stroke="#fff" stroke-width="1.3"/><circle cx="6" cy="3.4" r=".8" fill="#fff"/></svg>
    AI Disclaimer
  </div>

  <div class="tile" style="left:12px;top:44px">
    <div class="tile-label">Original ID: OLO9YDY5</div>
    <div class="tile-body photo-bw" role="img" aria-label="Black and white family portrait">
      <div class="dl"><svg width="14" height="14" viewBox="0 0 14 14" fill="none" stroke="#fff" stroke-width="1.3"><path d="M8.5 1H3.5A1.5 1.5 0 0 0 2 2.5v9A1.5 1.5 0 0 0 3.5 13h7a1.5 1.5 0 0 0 1.5-1.5V4.5z"/><path d="M7 5.5v5M5 8.5l2 2 2-2"/></svg></div>
    </div>
  </div>
  <div class="tile" style="left:268px;top:44px">
    <div class="tile-label">Vintage</div>
    <div class="tile-body">Not generated</div>
  </div>
  <div class="tile" style="left:524px;top:44px">
    <div class="tile-label">Real</div>
    <div class="tile-body">Not generated</div>
  </div>
  <div class="action action--outline" style="top:169px">
    <svg width="12" height="12" viewBox="0 0 12 12" fill="none" stroke="#16181d" stroke-width="1.2"><path d="M3 2.6A4.3 4.3 0 1 0 6 1.7"/><path d="M3 .8v2.2h2.2"/></svg>Rotate
  </div>
  <div class="action action--danger" style="top:200px">
    <svg width="10" height="11" viewBox="0 0 10 11"><path d="M1 2.5h8M3.5 2.5V1h3v1.5" stroke="#ef4444" stroke-width="1.1" fill="none"/><path d="M1.8 3.5h6.4l-.6 7H2.4z" fill="#ef4444"/></svg>Delete
  </div>
  <div class="action action--generate" style="top:231px">
    <svg width="12" height="12" viewBox="0 0 12 12" fill="#fff"><path d="M5 2 6 5 9 6 6 7 5 10 4 7 1 6 4 5z"/><path d="M9.5 .5 10 2l1.5.5L10 3l-.5 1.5L9 3 7.5 2.5 9 2z"/></svg>Generate (20)
  </div>

  <div class="divider"></div>

  <div class="tile" style="left:12px;top:282px">
    <div class="tile-label">Original ID: OLO9YDY5</div>
    <div class="tile-body photo-bw" role="img" aria-label="Black and white family portrait">
      <div class="dl"><svg width="14" height="14" viewBox="0 0 14 14" fill="none" stroke="#fff" stroke-width="1.3"><path d="M8.5 1H3.5A1.5 1.5 0 0 0 2 2.5v9A1.5 1.5 0 0 0 3.5 13h7a1.5 1.5 0 0 0 1.5-1.5V4.5z"/><path d="M7 5.5v5M5 8.5l2 2 2-2"/></svg></div>
    </div>
  </div>
  <div class="tile" style="left:268px;top:282px">
    <div class="tile-label">Vintage <span class="badge"><svg width="6" height="6" viewBox="0 0 6 6" fill="none" stroke="#1f9d55" stroke-width="1"><path d="M.8 3.2 2.3 4.6 5.2 1.4"/></svg>Done</span></div>
    <div class="tile-body photo-color" role="img" aria-label="Colorized family portrait, vintage tones">
      <div class="dl"><svg width="14" height="14" viewBox="0 0 14 14" fill="none" stroke="#fff" stroke-width="1.3"><path d="M8.5 1H3.5A1.5 1.5 0 0 0 2 2.5v9A1.5 1.5 0 0 0 3.5 13h7a1.5 1.5 0 0 0 1.5-1.5V4.5z"/><path d="M7 5.5v5M5 8.5l2 2 2-2"/></svg></div>
    </div>
  </div>
  <div class="tile" style="left:524px;top:282px">
    <div class="tile-label">Real</div>
    <div class="tile-body photo-color" role="img" aria-label="Colorized family portrait, real tones">
      <div class="dl"><svg width="14" height="14" viewBox="0 0 14 14" fill="none" stroke="#fff" stroke-width="1.3"><path d="M8.5 1H3.5A1.5 1.5 0 0 0 2 2.5v9A1.5 1.5 0 0 0 3.5 13h7a1.5 1.5 0 0 0 1.5-1.5V4.5z"/><path d="M7 5.5v5M5 8.5l2 2 2-2"/></svg></div>
    </div>
  </div>
  <div class="timing">
    <svg width="14" height="14" viewBox="0 0 14 14" fill="none" stroke="#9a9ea5" stroke-width="1.1"><circle cx="7" cy="7" r="6"/><circle cx="7" cy="7" r="3.6"/></svg>
    <p>Generation time:</p>
    <strong>3m 2s</strong>
  </div>
  <div class="action action--danger" style="top:469px">
    <svg width="10" height="11" viewBox="0 0 10 11"><path d="M1 2.5h8M3.5 2.5V1h3v1.5" stroke="#ef4444" stroke-width="1.1" fill="none"/><path d="M1.8 3.5h6.4l-.6 7H2.4z" fill="#ef4444"/></svg>Delete
  </div>
</section>
</body>
</html>
```